Painting Company Business Card

Brightwell Painting needs a new business card. See attachments for our logo and current card as an example.
We want to utilize the same colors in the logo, and keep all the information that is currently on it. Just need an updated and modern design.
We are open to loosing the Association Logos if it means a better design.
We are also entertaining a spot for a picture of a headshot of the person listed on the card. Head shot can be finished later.

```html
<!DOCTYPE html>
<html lang="en">
<head>
<meta charset="utf-8">
<title>Brightwell Painting – Business Card</title>
<link rel="stylesheet" href="https://fonts.googleapis.com/css2?family=Roboto:wght@400;500;700&display=swap">
<style>
  :root {
    --canvas-bg: #ecebe7;
    --card-green: #2e4632;
    --card-green-dark: #273c2b;
    --brand-green: #3f5a40;
    --brand-maroon: #6b3833;
    --paper: #ffffff;
    --text-light: #f2f2ee;
    --text-muted: #d9ded6;
    --photo-top: #d8dadc;
    --photo-bottom: #2b2d31;
  }
  * { box-sizing: border-box; margin: 0; padding: 0; }
  html, body { width: 1200px; height: 800px; overflow: hidden; }
  body {
    background: var(--canvas-bg);
    font-family: "Roboto", Arial, sans-serif;
    display: flex;
    align-items: center;
    justify-content: center;
    gap: 40px;
  }
  .card {
    width: 540px;
    height: 309px;
    position: relative;
    overflow: hidden;
    box-shadow: 0 10px 28px rgba(0,0,0,.18);
  }

  /* Back side */
  .card--back { background: var(--card-green); }
  .back__brand {
    position: absolute;
    top: 34px;
    right: 36px;
    display: flex;
    align-items: center;
    gap: 10px;
    color: var(--text-light);
    font-weight: 700;
    font-size: 20px;
  }
  .brand-square {
    width: 14px; height: 14px;
    background: var(--text-light);
  }
  .services {
    position: absolute;
    left: 48px;
    top: 110px;
    list-style: none;
  }
  .services li {
    display: flex;
    align-items: center;
    gap: 20px;
    color: var(--text-light);
    font-weight: 500;
    font-size: 19px;
    letter-spacing: 4px;
    height: 40px;
  }
  .services svg { width: 22px; height: 22px; flex: none; }

  /* Front side */
  .card--front { background: var(--paper); }
  .front__top {
    position: absolute;
    inset: 0 0 auto 0;
    height: 170px;
    background: var(--paper);
  }
  .front__brand {
    position: absolute;
    left: 34px;
    top: 46px;
    display: flex;
    align-items: center;
    gap: 12px;
    color: var(--brand-green);
    font-weight: 700;
    font-size: 34px;
    line-height: 1;
  }
  .front__brand .brand-square { background: var(--brand-maroon); width: 18px; height: 18px; }
  .headshot {
    position: absolute;
    right: 22px;
    top: 34px;
    width: 156px;
    height: 136px;
    background: linear-gradient(180deg, var(--photo-top) 0%, var(--photo-bottom) 100%);
  }
  .front__stripe {
    position: absolute;
    left: 0; right: 0;
    top: 170px;
    height: 7px;
    background: var(--brand-maroon);
  }
  .front__bottom {
    position: absolute;
    left: 0; right: 0; bottom: 0;
    top: 177px;
    background: var(--card-green);
    display: flex;
    align-items: center;
  }
  .person {
    width: 270px;
    text-align: right;
    padding-right: 22px;
    color: var(--text-light);
  }
  .person__name { font-size: 20px; font-weight: 400; }
  .person__role { font-size: 13px; color: var(--text-muted); margin-top: 4px; }
  .divider {
    width: 1px;
    height: 84px;
    background: var(--text-light);
  }
  .contacts {
    list-style: none;
    padding-left: 18px;
    color: var(--text-light);
    font-size: 14px;
  }
  .contacts li {
    display: flex;
    align-items: center;
    gap: 9px;
    height: 24px;
  }
  .contacts svg { width: 15px; height: 15px; flex: none; }
</style>
</head>
<body>

  <section class="card card--back" aria-label="Card back">
    <div class="back__brand"><span class="brand-square"></span>Brightwell Painting</div>
    <ul class="services">
      <li><svg viewBox="0 0 22 22"><rect x="1.5" y="3.5" width="16" height="16" rx="2" fill="none" stroke="#f2f2ee" stroke-width="2"/><path d="M5 11l4 4 11-12" fill="none" stroke="#f2f2ee" stroke-width="2.6" stroke-linecap="round"/></svg>Exterior Painting</li>
      <li><svg viewBox="0 0 22 22"><rect x="1.5" y="3.5" width="16" height="16" rx="2" fill="none" stroke="#f2f2ee" stroke-width="2"/><path d="M5 11l4 4 11-12" fill="none" stroke="#f2f2ee" stroke-width="2.6" stroke-linecap="round"/></svg>Interior Painting</li>
      <li><svg viewBox="0 0 22 22"><rect x="1.5" y="3.5" width="16" height="16" rx="2" fill="none" stroke="#f2f2ee" stroke-width="2"/><path d="M5 11l4 4 11-12" fill="none" stroke="#f2f2ee" stroke-width="2.6" stroke-linecap="round"/></svg>Carpentry</li>
      <li><svg viewBox="0 0 22 22"><rect x="1.5" y="3.5" width="16" height="16" rx="2" fill="none" stroke="#f2f2ee" stroke-width="2"/><path d="M5 11l4 4 11-12" fill="none" stroke="#f2f2ee" stroke-width="2.6" stroke-linecap="round"/></svg>Drywall</li>
    </ul>
  </section>

  <section class="card card--front" aria-label="Card front">
    <div class="front__top">
      <div class="front__brand"><span class="brand-square"></span>Brightwell Painting</div>
      <div class="headshot" role="img" aria-label="Headshot of Mark Delaney in a dark suit"></div>
    </div>
    <div class="front__stripe"></div>
    <div class="front__bottom">
      <div class="person">
        <p class="person__name">Mark Delaney</p>
        <p class="person__role">Quality Manager</p>
      </div>
      <div class="divider"></div>
      <ul class="contacts">
        <li><svg viewBox="0 0 16 16"><circle cx="8" cy="8" r="8" fill="#f2f2ee"/><path d="M5.2 4.2l1.6-.3.8 2-1 .8a5 5 0 0 0 2.7 2.7l.8-1 2 .8-.3 1.6c-3.8.4-7-2.8-6.6-6.6z" fill="#2e4632"/></svg>262-555-0147</li>
        <li><svg viewBox="0 0 16 16"><circle cx="8" cy="8" r="8" fill="#f2f2ee"/><rect x="4" y="5.3" width="8" height="5.4" fill="#2e4632"/><path d="M4 5.5l4 3 4-3" fill="none" stroke="#f2f2ee" stroke-width=".9"/></svg>Mark.Brightwell@mailbox.com</li>
        <li><svg viewBox="0 0 16 16"><circle cx="8" cy="8" r="8" fill="#f2f2ee"/><circle cx="8" cy="8" r="4.6" fill="none" stroke="#2e4632" stroke-width="1"/><ellipse cx="8" cy="8" rx="2" ry="4.6" fill="none" stroke="#2e4632" stroke-width="1"/><path d="M3.4 8h9.2" stroke="#2e4632" stroke-width="1"/></svg>BrightwellPainting.com</li>
      </ul>
    </div>
  </section>

</body>
</html>
```